Zielgruppe
Ich bin eine junge Fotografin und tätig in folgenden Bereichen:
- Hochzeits-Fotografie
- Outdoor-Fotografie
- Studio-Fotografie
Aufgabenstellung
Die Seite soll freundlich, professionell und übersichtlich sein.
Die Seite soll von den Bildern leben. Emotionen vermitteln.
Responsive Design ist mir wichtig, im nachhinein möchte ich die Seite Programmieren lassen damit ich mit Wordpress arbeiten kann und die Seite soll gut Suchmaschinenoptimiert werden.

```html
<!DOCTYPE html>
<html lang="de">
<head>
<meta charset="utf-8">
<title>Velvet Lantern – Fotografie</title>
<link href="https://fonts.googleapis.com/css2?family=Open+Sans:wght@300;400;700&family=Roboto:wght@400&display=swap" rel="stylesheet">
<style>
:root{
  --red:#d9050c;
  --ink:#1e1e1e;
  --nav:#444;
  --white:#fff;
  --footer:#5a5a5a;
}
*{margin:0;padding:0;box-sizing:border-box}
html,body{width:1200px;height:723px;overflow:hidden;background:var(--white);font-family:"Open Sans",sans-serif}
.page{position:relative;width:1200px;height:723px;border-top:2px solid var(--red)}
.site-header{position:absolute;top:0;left:0;width:1200px;height:58px;background:var(--white);box-shadow:0 1px 3px rgba(0,0,0,.12);z-index:2}
.brand{position:absolute;left:200px;top:17px;display:flex;align-items:center;gap:7px;font-size:19px;font-weight:400;color:var(--ink);letter-spacing:.02em}
.brand-dot{width:9px;height:9px;border-radius:50%;background:var(--red)}
.main-nav{position:absolute;top:21px;left:702px;display:flex;align-items:center;font-family:"Roboto",sans-serif;font-size:8.5px;color:var(--nav)}
.main-nav a{color:inherit;text-decoration:none;margin-right:18px}
.main-nav a.active{background:var(--red);color:var(--white);padding:5px 8px;margin-right:11px}
.hero{position:absolute;top:58px;left:0;width:1200px;height:315px;
  background:
    radial-gradient(ellipse 150px 130px at 33% 52%,rgba(150,150,150,.55),rgba(150,150,150,0) 100%),
    radial-gradient(ellipse 260px 200px at 25% 45%,rgba(120,120,120,.35),rgba(120,120,120,0) 100%),
    radial-gradient(ellipse 130px 190px at 80% 55%,rgba(110,110,110,.45),rgba(110,110,110,0) 100%),
    radial-gradient(ellipse 90px 100px at 79% 30%,rgba(200,200,200,.6),rgba(200,200,200,0) 100%),
    linear-gradient(180deg,#e4e4e4 0%,#dadada 60%,#ececec 100%)}
.hero-title{position:absolute;left:159px;top:128px;font-size:29.7px;font-weight:300;color:var(--ink);white-space:nowrap}
.hero-title em{font-style:normal;color:var(--red)}
.hero-tags{position:absolute;left:628px;top:170px;font-size:12.4px;font-weight:400;color:#333;letter-spacing:.02em;white-space:nowrap}
.tiles{position:absolute;top:373px;left:0;width:1200px;height:190px;display:flex}
.tile{position:relative;width:300px;height:190px}
.tile-1{background:
  radial-gradient(ellipse 70px 22px at 12% 46%,rgba(40,40,40,.55),rgba(40,40,40,0) 100%),
  radial-gradient(ellipse 70px 22px at 80% 72%,rgba(40,40,40,.55),rgba(40,40,40,0) 100%),
  linear-gradient(180deg,#e0e0e0 0%,#bdbdbd 55%,#d6d6d6 100%)}
.tile-2{background:
  radial-gradient(ellipse 120px 80px at 52% 48%,rgba(35,35,35,.75),rgba(35,35,35,0) 100%),
  linear-gradient(160deg,#ececec,#d6d6d6)}
.tile-3{background:
  radial-gradient(ellipse 120px 90px at 45% 45%,rgba(90,90,90,.55),rgba(90,90,90,0) 100%),
  linear-gradient(160deg,#cfcfcf,#b0b0b0)}
.tile-4{background:
  radial-gradient(ellipse 40px 95px at 90% 50%,rgba(20,20,20,.85),rgba(20,20,20,0) 100%),
  linear-gradient(90deg,#d4d4d4,#bebebe)}
.tile-label{position:absolute;left:0;right:0;top:83px;text-align:center;font-size:14.4px;font-weight:700;letter-spacing:.2em;color:#111}
.tile-rule{position:absolute;left:50%;top:112px;width:63px;height:2px;margin-left:-31px;background:var(--red)}
.tile-frame{position:absolute;left:56px;top:70px;width:190px;height:44px;border:1px solid var(--red)}
.site-footer{position:absolute;top:563px;left:0;width:1200px;height:160px;background:var(--footer);color:var(--white);text-align:center;font-size:10.7px;line-height:17.1px;padding-top:16px}
.site-footer a{color:var(--white)}
.site-footer strong{font-weight:700}
.social-box{display:inline-block;width:19px;height:19px;background:#111;vertical-align:middle;margin-left:3px}
</style>
</head>
<body>
<div class="page">
  <header class="site-header">
    <div class="brand"><span>Velvet Lantern</span><span class="brand-dot"></span></div>
    <nav class="main-nav">
      <a class="active" href="#">Willkommen</a>
      <a href="#">Hinter der Linse</a>
      <a href="#">Portfolio</a>
      <a href="#">Angebote</a>
      <a href="#">Kontakt</a>
    </nav>
  </header>

  <section class="hero" role="img" aria-label="Helles Schwarzweissfoto: Kameraobjektiv links, lächelnde Fotografin mit Kamera rechts">
    <h1 class="hero-title"><em>Herzlich Willkommen</em> in der Welt der Fotografie</h1>
    <p class="hero-tags">HOCHZEIT | OUTDOOR | STUDIO</p>
  </section>

  <section class="tiles">
    <div class="tile tile-1" role="img" aria-label="Schwarzweissfoto einer Augenpartie">
      <div class="tile-label">HINTER DER LINSE</div><div class="tile-rule"></div>
    </div>
    <div class="tile tile-2" role="img" aria-label="Schwarzweissfoto eines Fotobuchs">
      <div class="tile-frame"></div>
      <div class="tile-label">PORTFOLIO</div><div class="tile-rule"></div>
    </div>
    <div class="tile tile-3" role="img" aria-label="Schwarzweissfoto eines Handschlags">
      <div class="tile-label">ANGEBOTE</div><div class="tile-rule"></div>
    </div>
    <div class="tile tile-4" role="img" aria-label="Schwarzweissfoto eines Telefonhörers">
      <div class="tile-label">KONTAKT</div><div class="tile-rule"></div>
    </div>
  </section>

  <footer class="site-footer">
    <div>© www.velvet-lantern.ch. Alle Rechte vorbehalten. <a href="#">AGB</a> I <a href="#">Links</a></div>
    <div><strong>Velvet Lantern | Fotografie</strong></div>
    <div><strong>Lena Brunner</strong></div>
    <div>Lindenweg 14</div>
    <div>6300 Talbach</div>
    <div>Mobile: 079 555 18 27</div>
    <div>Netzwerk: <span class="social-box"></span></div>
  </footer>
</div>
</body>
</html>
```